ecwid kavrel design app kavrel-cosmetology

need app shop for my store
i have app option in my store, can activate, need design with slider
same need blog for shop
aaassssssssssssssssssssaaaaaaaas

same need blog for shop
same need blog for shop

Target Market(s)

kosmetic beauty aesthetic

Font styles to use
Serif
Sans Serif

Colors
33a6d7
85abd3
00a990
cfeae6
cee9f5

Requirements
Must have
• my projet can you looking on kavrel.de
Nice to have
• blue design wirh grey

```html
<!DOCTYPE html>
<html lang="de">
<head>
<meta charset="utf-8">
<title>kavrel cosmetology – Shop App</title>
<link rel="stylesheet" href="https://fonts.googleapis.com/css2?family=Roboto:wght@300;400;500;700&display=swap">
<style>
  :root{
    --bg:#eef1f5;
    --ink:#16171b;
    --ink-line:#24262c;
    --menu-text:#e6e7ea;
    --gold:#c9964a;
    --blue:#1e90ff;
    --white:#ffffff;
    --card-line:#e4e6ea;
    --grey-text:#9a9ca2;
    --dark-text:#1a1a1a;
    --orange:#e08a3c;
    --overlay:#5e5f63;
  }
  *{box-sizing:border-box;margin:0;padding:0}
  html,body{width:1200px;height:1200px;overflow:hidden}
  body{background:var(--bg);font-family:"Roboto",Arial,sans-serif;position:relative}
  .screen{position:absolute;top:280px;width:360px;height:640px;background:var(--ink);overflow:hidden;border-radius:4px;box-shadow:0 20px 50px rgba(30,40,60,.12)}
  .screen--menu{left:190px}
  .screen--shop{left:650px;background:var(--white)}
  .status-bar{height:20px;display:flex;justify-content:space-between;align-items:center;padding:0 8px;color:var(--white);font-size:10px;background:var(--ink)}
  .battery{display:inline-block;width:20px;height:9px;border:1px solid var(--white);border-radius:2px;background:var(--white);vertical-align:middle;margin-left:3px}
  .app-header{height:58px;background:var(--ink);position:relative;display:flex;align-items:center;justify-content:center}
  .brand{color:var(--gold);font-size:20px;font-weight:400;letter-spacing:1px;display:flex;align-items:center;gap:7px}
  .brand-dot{width:8px;height:8px;border-radius:50%;background:var(--gold)}
  .header-icons{position:absolute;right:12px;top:18px;display:flex;gap:12px}
  .burger{position:absolute;left:14px;top:22px}
  .cart{position:relative}
  .cart-count{position:absolute;top:-5px;right:-5px;width:9px;height:9px;border-radius:50%;background:var(--blue)}
  /* menu */
  .menu{position:absolute;left:0;top:78px;width:250px;bottom:0;background:var(--ink);z-index:2}
  .menu-item{height:42px;line-height:42px;padding-left:22px;color:var(--menu-text);font-size:14px;font-weight:300;border-bottom:1px solid var(--ink-line)}
  .menu-shade{position:absolute;left:250px;right:0;top:78px;bottom:0;background:var(--overlay)}
  /* tabs */
  .tabs{height:36px;background:var(--ink);display:flex}
  .tab{flex:1;color:#6c6e74;font-size:12px;text-align:center;line-height:36px}
  .tab--active{background:var(--blue);color:var(--white);position:relative}
  .tab--active::after{content:"";position:absolute;left:50%;bottom:-6px;margin-left:-6px;border:6px solid transparent;border-bottom:0;border-top-color:var(--blue)}
  .products{padding:8px 10px}
  .product{display:flex;gap:14px;align-items:center;padding:14px 6px;border-bottom:1px solid var(--card-line);height:172px}
  .product-photo{width:120px;height:110px;border-radius:4px;flex:none}
  .photo--gold{background:linear-gradient(160deg,#f4d46a,#d59a2a)}
  .photo--violet{background:linear-gradient(160deg,#8a4aa8,#4c1e6a)}
  .photo--silver{background:linear-gradient(160deg,#f1f2f4,#b9bcc4)}
  .badge{display:inline-block;background:var(--ink);color:var(--white);font-size:8px;padding:2px 4px;margin-bottom:4px}
  .product-name{font-size:15px;font-weight:300;color:var(--dark-text);margin-bottom:3px}
  .product-brand,.product-type{font-size:9px;color:var(--grey-text);line-height:1.5}
  .price{font-size:10px;font-weight:700;color:var(--dark-text);margin-top:4px;line-height:1.5}
  .price span{color:var(--orange);font-weight:400}
</style>
</head>
<body>

<section class="screen screen--menu">
  <div class="status-bar"><span>●●●●● Carrier</span><span>9:41 AM</span><span>100%<i class="battery"></i></span></div>
  <header class="app-header">
    <svg class="burger" width="12" height="10" viewBox="0 0 12 10"><path d="M0 1h12M0 5h12M0 9h12" stroke="#fff" stroke-width="1.4"/></svg>
    <div class="brand"><i class="brand-dot"></i>kavrel</div>
    <div class="header-icons">
      <svg width="14" height="14" viewBox="0 0 14 14"><circle cx="6" cy="6" r="4.5" fill="none" stroke="#fff" stroke-width="1.3"/><path d="M9.5 9.5L13 13" stroke="#fff" stroke-width="1.3"/></svg>
      <svg width="16" height="14" viewBox="0 0 16 14"><path d="M1 1h2.5l2 8h8l1.5-6H4.3" fill="none" stroke="#fff" stroke-width="1.2"/><circle cx="6.5" cy="12" r="1.2" fill="#fff"/><circle cx="12.5" cy="12" r="1.2" fill="#fff"/></svg>
    </div>
  </header>
  <nav class="menu">
    <div class="menu-item">Start</div>
    <div class="menu-item">Düfte</div>
    <div class="menu-item">Make-up</div>
    <div class="menu-item">Pflege</div>
    <div class="menu-item">Haare</div>
    <div class="menu-item">Accessoires</div>
    <div class="menu-item">AlleMarken</div>
    <div class="menu-item">Sale</div>
    <div class="menu-item">Hot Products</div>
    <div class="menu-item">GratisGeschenke</div>
    <div class="menu-item">Weihnachten</div>
    <div class="menu-item">KVL Blog</div>
  </nav>
  <div class="menu-shade"></div>
</section>

<section class="screen screen--shop">
  <div class="status-bar"><span>●●●●● Carrier</span><span>9:41 AM</span><span>100%<i class="battery"></i></span></div>
  <header class="app-header">
    <svg class="burger" width="12" height="10" viewBox="0 0 12 10"><path d="M0 1h12M0 5h12M0 9h12" stroke="#fff" stroke-width="1.4"/></svg>
    <div class="brand"><i class="brand-dot"></i>kavrel</div>
    <div class="header-icons">
      <svg width="14" height="14" viewBox="0 0 14 14"><circle cx="6" cy="6" r="4.5" fill="none" stroke="#fff" stroke-width="1.3"/><path d="M9.5 9.5L13 13" stroke="#fff" stroke-width="1.3"/></svg>
      <span class="cart"><svg width="16" height="14" viewBox="0 0 16 14"><path d="M1 1h2.5l2 8h8l1.5-6H4.3" fill="none" stroke="#fff" stroke-width="1.2"/><circle cx="6.5" cy="12" r="1.2" fill="#fff"/><circle cx="12.5" cy="12" r="1.2" fill="#fff"/></svg><i class="cart-count"></i></span>
    </div>
  </header>
  <div class="tabs">
    <div class="tab tab--active">Düfte</div>
    <div class="tab">Pflege</div>
    <div class="tab">Make-up</div>
  </div>
  <div class="products">
    <article class="product">
      <div class="product-photo photo--gold" role="img" aria-label="Golden perfume bottle"></div>
      <div>
        <span class="badge">NEU</span>
        <h3 class="product-name">Varenne</h3>
        <p class="product-brand">Nordia</p>
        <p class="product-type">Eau de Parfum Spray</p>
        <p class="price">190,00 € / <span>50 ml</span><br>GP: 380,00€ / <span>100 ml</span></p>
      </div>
    </article>
    <article class="product">
      <div class="product-photo photo--violet" role="img" aria-label="Purple product box"></div>
      <div>
        <span class="badge">NEU</span>
        <h3 class="product-name">Lumaderm Ultra 2</h3>
        <p class="product-brand">Nordia</p>
        <p class="product-type">Eau de Parfum Spray</p>
        <p class="price">190,00 € / <span>50 ml</span><br>GP: 380,00€ / <span>100 ml</span></p>
      </div>
    </article>
    <article class="product">
      <div class="product-photo photo--silver" role="img" aria-label="Silver product box"></div>
      <div>
        <span class="badge">NEU</span>
        <h3 class="product-name">Lumaderm Ultra</h3>
        <p class="product-brand">Nordia</p>
        <p class="product-type">Eau de Parfum Spray</p>
        <p class="price">190,00 € / <span>50 ml</span><br>GP: 380,00€ / <span>100 ml</span></p>
      </div>
    </article>
  </div>
</section>

</body>
</html>
```